Create for us a Shop-Stopper Business Card

We need a standout, first class business card to go along with our new brand strategy. Sleek, Contemporary and fresh.

Colors and theme must sync with our websitewww.pelvorpower.co.uk

We want a business card that has a global brand appeal. TKR Energy is a small UK renewable company that specialises in energy projects in Africa. We want a business card that has the following characteristics: Very short, precise, global, stand out, NOT TOO LOUD but contemporary. The company's colour themes are White, Grey with a hint of green.

Target Market(s)

Business exec, high net worth individuals, investors, commercial leaders, suppliers, government officials

Industry/Entity Type

Solar Energy

Contact Information for Business Card

Logo, Name, Title, Address, web address, email,

Requirements
Must have
• Logo must be sharp
Nice to have
• Adapt fonts from the logo. The large circular side of the logo at the back in a very refreshing way
Should not have
• No solar panel shapes or image.Very little black. If possible avoid black. Its not coming out nice. I think !!!

```html
<!DOCTYPE html>
<html lang="en">
<head>
<meta charset="utf-8">
<title>TKR Energy – Business Card</title>
<link rel="stylesheet" href="https://fonts.googleapis.com/css2?family=Figtree:wght@400;600;700&display=swap">
<style>
  :root {
    --backdrop: #30363a;
    --paper: #ffffff;
    --green-dark: #0b7a3a;
    --green-mid: #2e9e44;
    --green-light: #6cc43a;
    --green-lime: #8cc63f;
    --ink: #2b2b2b;
    --ink-name: #3a3a3a;
    --accent-red: #c0272d;
  }
  * { margin: 0; padding: 0; box-sizing: border-box; }
  html, body { width: 1200px; height: 661px; overflow: hidden; }
  body {
    background: var(--backdrop);
    font-family: "Figtree", "Helvetica Neue", Arial, sans-serif;
    position: relative;
  }
  .card {
    position: absolute;
    width: 565px;
    height: 344px;
    overflow: hidden;
  }
  /* Front */
  .card--front { left: 24px; top: 156px; background: var(--paper); }
  .front__mark {
    position: absolute; left: 50px; top: 68px;
    width: 160px; height: 160px; border-radius: 50%;
    background: var(--green-dark);
  }
  .front__name {
    position: absolute; left: 240px; top: 100px;
    font-size: 40px; font-weight: 600; letter-spacing: 1px;
    color: var(--ink-name); line-height: 1;
  }
  .front__rule {
    position: absolute; left: 240px; top: 144px;
    width: 254px; height: 2px; background: var(--accent-red);
  }
  .front__band {
    position: absolute; left: 180px; top: 160px; right: 0; height: 34px;
    background: var(--green-dark);
  }
  .front__tagline {
    position: absolute; left: 240px; top: 164px;
    font-size: 21px; font-weight: 700; color: var(--paper); line-height: 26px;
  }
  .front__address {
    position: absolute; left: 240px; top: 206px;
    font-size: 16px; color: var(--ink);
  }
  .front__contact {
    position: absolute; left: 240px; top: 240px;
    font-size: 16px; line-height: 22px; color: var(--ink);
  }
  .front__contact b { font-weight: 700; }
  .front__contact .web { color: var(--green-dark); }
  .front__stripe {
    position: absolute; left: 0; bottom: 0; width: 100%; height: 8px;
    background: linear-gradient(to right, var(--green-light) 0 246px, var(--green-dark) 246px 100%);
  }
  /* Back */
  .card--back {
    left: 614px; top: 154px; height: 346px;
    background: linear-gradient(225deg, var(--green-lime) 0%, var(--green-mid) 55%, var(--green-dark) 100%);
    color: var(--paper); text-align: center;
  }
  .back__mark {
    position: absolute; left: 50%; top: 60px; transform: translateX(-50%);
    width: 100px; height: 100px; border-radius: 50%;
    border: 10px solid var(--paper);
  }
  .back__name {
    position: absolute; left: 0; right: 0; top: 180px;
    font-size: 28px; font-weight: 600; letter-spacing: 1px;
  }
  .back__tagline {
    position: absolute; left: 0; right: 0; top: 264px;
    font-size: 29px; font-weight: 700;
  }
</style>
</head>
<body>
  <section class="card card--front">
    <div class="front__band"></div>
    <div class="front__mark"></div>
    <div class="front__name">TKR ENERGY</div>
    <div class="front__rule"></div>
    <div class="front__tagline">Lets Do The Impossible!</div>
    <p class="front__address">N7 4QX, London, United Kingdom</p>
    <p class="front__contact">
      <b>E.</b> xxxx pelvorpower.co.uk<br>
      <span class="web"><b>W.</b> www.pelvorpower.co.uk</span>
    </p>
    <div class="front__stripe"></div>
  </section>

  <section class="card card--back">
    <div class="back__mark"></div>
    <div class="back__name">TKR Energy</div>
    <div class="back__tagline">Lets Do The Impossible!</div>
  </section>
</body>
</html>
```